Research Program Web Site

Goal:
-Create photoshop or HTML+CSS mockup of homepage for the Program for Knowledge Systems .
- Also create a child page which would be used to frame more detailed information - e.g. a list of publications, blog page, project activities, staff page.
Details:
The homepage is intended to convey:
- The mission of the program
- Link to overviews of research projects, preferably with brief teaser descriptions
- Display information on upcoming events, publications and tweets
- Show a connection to Varnell and the Varnell libraries
- Encourage viewers to follow/share content via social studio
Target audience:
- Research funders interested in an overview of the program, its major research areas, and research outputs (such as program publications and software, awards)
- Varnell community (faculty, library staff, and students) interested in current information (blogs/tweets), events, and possible collaboration opportunities
Hosting:
- The site will eventually be hosted on datahub.varnell.edu using a CMS (Quillet)
- There will be opportunity for further website implementation work if desired
Existing material:
- A text overview of the research program is included in the appendix attached to this document
- Much of the information on research projects is currently described here: http://drbkessler.blogvista.example/dr-kesslers-current-projects-and-research-aka-what-is-jonas-doing/ This content will be moved to the program site when completed.
Themes:
- Varnell color scheme is here, it is not required, but could be used for inspiration: http://web.varnell.edu/graphicidentity/colors/index.html
- Varnell libraries home page is here: http://libraries.varnell.edu/.
- The program page should borrow some design element from the library page if possible, and include the library and Varnell logos somewhere on the page - but not as the most prominent branding element.
- Overall look and feel should be professional and serious, but modern
Comparison sites:
For comparison here are several pages for similar sites that are done fairly well:
http://www.dornsurvey.org/
http://www.studio.varnell.edu/
http://www.qs.bellmore.edu/
- The dorn and studio sites have the cleanest design.
- Both dorn and qs are successful in conveying information about upcoming evevnts, publication and tweets
- Studio lab shows the right connection to larger organization
- Dorn site communicates better the mission of the organization
Updates
A number of you have noted that the program description attachment was missing. I have now uploaded it. Thanks much - Jonas
Thanks to those who have submitted designs so far. I have noticed that none of the designs thus far submitted include all of the elements requested in the design brief (task description). For clarification, I will emphasize these required elements:
- an area to describe the mission of the program
4. Branding/theming
Reason: Provide additional time for review of designs by colleagues on this end
Thanks,
Jonas
Target Market(s)
- Research funders interested in an overview of the program, its major research areas, and research outputs (such as program publications and software
Industry/Entity Type
Library
Requirements
Nice to have
- hemes:
Comparison sites:
http://www.studio.varnell.edu/

```html
<!DOCTYPE html>
<html lang="en">
<head>
<meta charset="utf-8">
<title>Program for Knowledge Systems</title>
<link rel="stylesheet" href="https://fonts.googleapis.com/css2?family=Arimo:wght@400;700&display=swap">
<style>
:root{
  --brand:#8f2d2e;
  --brand-soft:#c9a0a2;
  --text:#4a4a4a;
  --muted:#6d6d6d;
  --rule:#d9b9ba;
  --panel:#ececec;
  --white:#ffffff;
}
*{box-sizing:border-box;margin:0;padding:0}
html,body{width:1200px;height:1200px;overflow:hidden;background:var(--white)}
body{position:relative;font-family:"Arimo",Arial,sans-serif;color:var(--text)}
.abs{position:absolute}
.masthead{left:0;top:0;width:1200px;height:108px;background:var(--brand)}
.masthead-right{left:744px;top:0;width:456px;height:138px;background:var(--brand);clip-path:polygon(0 0,100% 0,100% 100%,30px 100%,15px 78%,0 78%)}
.site-title{left:222px;top:60px;font-size:23px;color:var(--white);font-weight:400}
.search{left:759px;top:86px;width:152px;height:18px;background:#f1f1f1;border:1px solid #ccc;font-size:13px;color:#888;padding-left:3px;line-height:16px}
.search svg{position:absolute;right:3px;top:2px}
.social{top:91px;width:11px;height:11px;border-radius:50%;background:var(--white)}
.nav{left:224px;top:118px;display:flex;font-size:14px;color:#444}
.nav span{margin-right:17px}
.nav .sep{color:var(--brand)}
.nav .current{color:var(--brand);position:relative}
.nav .current::after{content:"";position:absolute;left:2px;bottom:-6px;border:3px solid transparent;border-top-color:var(--brand)}
.about-label{left:772px;top:119px;font-size:14px;color:var(--white);font-weight:700}
.about-bar{left:760px;top:138px;width:220px;height:12px;background:#ececec}
.hero{left:224px;top:150px;width:520px;height:261px;background:var(--brand)}
.hero-photo{left:233px;top:158px;width:502px;height:204px;background:radial-gradient(circle at 55% 40%,#f4f2ee 0,#c9c6c0 45%,#6e6a64 100%)}
.hero-caption{left:233px;top:337px;width:502px;height:25px;background:rgba(60,60,60,.55);color:var(--white);font-size:11px;padding:7px 7px}
.hero-tag{left:664px;top:158px;width:71px;height:20px;background:var(--brand);color:var(--white);font-size:11px;padding:3px 0 0 23px;clip-path:polygon(0 0,100% 0,100% 100%,16px 100%)}
.dropdown{left:518px;top:145px;width:108px;height:112px;background:rgba(190,100,105,.6);clip-path:polygon(0 0,92% 0,100% 6%,100% 100%,6% 100%,0 94%)}
.dropdown li{list-style:none;font-size:9.5px;color:var(--white);position:absolute;left:6px}
.tabs{top:370px;height:41px;color:var(--white);font-size:12.5px;font-weight:700;letter-spacing:.4px}
.tab-safe{left:224px;width:172px;background:var(--brand);clip-path:polygon(0 0,100% 0,100% 100%,22px 100%);padding:14px 0 0 27px}
.tab-open{left:396px;width:174px;border-left:1px solid #fff;padding:4px 0 0 12px;line-height:19px}
.tab-map{left:570px;width:174px;border-left:1px solid #fff;padding:14px 0 0 11px}
.mission{left:760px;top:150px;width:220px;height:261px;background:var(--brand);color:var(--white);font-size:13px;line-height:19.2px;padding:8px 10px 0 12px}
.mission a{position:absolute;left:103px;top:236px;font-size:11px;color:#e9d3d3;text-decoration:underline}
.feed-tabs{left:415px;top:440px;width:165px;height:20px}
.feed-tabs div{position:absolute;top:0;height:20px;color:var(--white);font-size:11px;padding-top:4px;background:var(--brand)}
.divider{left:484px;top:460px;width:2px;height:615px;background:var(--brand-soft)}
.col{top:470px;width:246px}
.col-news{left:224px}
.col-pubs{left:500px}
.item{border-bottom:1px solid var(--rule);padding:4px 0 14px;margin-bottom:14px}
.date{font-size:10.5px;color:#666;letter-spacing:.6px;margin-bottom:6px}
.news-text{font-size:12px;line-height:16px;color:var(--muted)}
.news-text.lead{color:var(--brand)}
.badge{display:inline-block;background:var(--brand);color:#fff;font-size:6px;padding:0 4px;position:absolute;top:-9px;left:0;clip-path:polygon(0 0,100% 0,85% 100%,0 100%)}
.pub-title{font-size:12.5px;letter-spacing:.5px;color:#555;line-height:16px;margin-bottom:6px;font-weight:400}
.pub-text{font-size:12px;line-height:16px;color:var(--muted)}
.more{text-align:right;font-size:11px;color:#666;text-decoration:underline}
.chirp{left:760px;top:430px;width:220px;height:645px;background:var(--panel);clip-path:polygon(0 0,100% 0,100% 100%,40px 100%,0 590px)}
.chirp-head{left:768px;top:438px;font-size:15px;font-weight:700;color:var(--brand)}
.chirp-tab-pop{left:877px;top:440px;font-size:11px;font-weight:700;color:var(--brand)}
.chirp-tab-latest{left:926px;top:436px;width:46px;height:22px;background:var(--brand);color:#fff;font-size:11px;font-weight:700;padding:5px 0 0 7px;clip-path:polygon(5px 0,100% 0,100% 100%,0 100%)}
.scroll{left:972px;top:461px;width:8px;height:200px;background:#c8c8c8}
.tweets{left:773px;top:470px;width:197px}
.tweet{height:70.4px;border-bottom:1px solid #bbb;padding-top:2px}
.tweet .ago{font-size:9px;color:#c98b8d;letter-spacing:.3px}
.tweet .ago b{font-size:10.5px;color:var(--brand)}
.tweet .t{font-size:9.5px;font-weight:700;color:var(--brand);line-height:14.4px;margin-top:5px}
.tweet-to{left:798px;top:1036px;font-size:11px;color:#555;font-weight:700}
.tweet-to small{display:block;font-size:9px;margin-top:1px}
.footer-bar{left:224px;top:1075px;width:757px;height:8px;background:var(--brand)}
.foot-brand{top:1118px;font-size:14px;font-weight:700;color:#555;white-space:nowrap}
.foot-link{top:1128px;font-size:11px;color:#555;letter-spacing:.4px}
.foot-icon{top:1127px;width:10px;height:10px;border-radius:50%;background:#777}
</style>
</head>
<body>
<header>
  <div class="abs masthead"></div>
  <div class="abs masthead-right"></div>
  <h1 class="abs site-title">Program for Knowledge Systems</h1>
  <div class="abs search">Search
    <svg width="12" height="12" viewBox="0 0 12 12"><circle cx="5" cy="5" r="3.5" fill="none" stroke="#555" stroke-width="1.6"/><line x1="7.5" y1="7.5" x2="11" y2="11" stroke="#555" stroke-width="1.8"/></svg>
  </div>
  <span class="abs social" style="left:923px" aria-label="Chirper"></span>
  <span class="abs social" style="left:945px" aria-label="Facepage"></span>
  <span class="abs social" style="left:968px" aria-label="News feed"></span>
  <nav class="abs nav">
    <span>Projects</span><span class="sep">\</span>
    <span>Publications</span><span class="sep">\</span>
    <span>Events</span><span class="sep">\</span>
    <span class="current">Sponsorship</span>
  </nav>
  <div class="abs about-label">About</div>
  <div class="abs about-bar"></div>
</header>

<section>
  <div class="abs hero"></div>
  <div class="abs hero-photo" role="img" aria-label="Soft-focus photograph of red archival blocks on a pale desk"></div>
  <div class="abs hero-caption">SafeVault is a solution for archival storage and replication management.</div>
  <div class="abs hero-tag">Project</div>
  <ul class="abs dropdown">
    <li style="top:18px">Levels of sponsorship</li>
    <li style="top:42px">Sponor list</li>
    <li style="top:65px">FAQ</li>
  </ul>
  <div class="abs tabs tab-safe">SafeVault</div>
  <div class="abs tabs tab-open">Open Scholar<br>&amp; Author Registry</div>
  <div class="abs tabs tab-map">Civic Districting Project</div>
</section>

<aside class="abs mission">
  The Varnell libraries have a history of innovative research. "From an early vision of a distributed system of discipline-oriented libraries, through the post-war futuristic ideals of Project Meridex, to the large-scale implementation of off-site storage in the 1970s, the Libraries have experimented with creative approaches to library and information service.
  <a>more information...</a>
</aside>

<div class="abs feed-tabs">
  <div style="left:0;width:69px;padding-left:23px;clip-path:polygon(0 0,100% 0,100% 100%,14px 100%)">Events</div>
  <div style="left:70px;width:95px;padding-left:12px;clip-path:polygon(0 0,100% 0,88% 100%,0 100%)">Publications</div>
</div>
<div class="abs divider"></div>

<section class="abs col col-news">
  <div class="item" style="position:relative">
    <span class="badge">NEW</span>
    <div class="date">NOV . 15 , 12 &nbsp;- &nbsp;NOV .20 ,12</div>
    <p class="news-text lead">Slides posted from the International Colloquium on Redistricting, hosted by the Instituto Cívico Regional.</p>
  </div>
  <div class="item"><div class="date">OCT . 25 , 12</div><p class="news-text">Report posted from the NRF/CSU Curating for Data Quality workshop.</p></div>
  <div class="item"><div class="date">OCT . 23 , 12</div><p class="news-text">Slides posted from the 2012 KLN Community Meeting.</p></div>
  <div class="item"><div class="date">OCT . 15 , 12</div><p class="news-text">Our WardMaker software wins the 2012 Data Innovation Award for social impact from Halloway Stratum.</p></div>
  <div class="item"><div class="date">AUG . 27 , 12</div><p class="news-text">Slides from Needs for Data Management &amp; Citation Throughout the Information Lifecycle (NIDA Forum, September 2012) posted</p></div>
  <div class="item"><div class="date">AUG . 27 , 12</div><p class="news-text">Joined the Task Force on Registering Researchers in Authority Files, OLRC Research.</p></div>
  <p class="more">more news...</p>
</section>

<section class="abs col col-pubs">
  <div class="item"><div class="date">DEC . 25 , 12</div><h3 class="pub-title">Auditing Distributed Preservation</h3><p class="pub-text">The core ideas around distributed digital preservation are well-recognized in the library and archival communities. Geographically distributed replication of content has been clearly identified for at least a decade as a best practice for management of digital content to which one must provide long-term access......</p></div>
  <div class="item"><div class="date">OCT . 25 , 12</div><h3 class="pub-title">Amberon's Creeping 'Moraine' and Digital Preservation</h3><p class="pub-text">Amberon recently announced integration of their core B7 service with their Moraine low-cost storage. This adds the ability to add rules to B7 (or their reduced redundancy store) to based on age, date, and B7 bucket prefix......</p></div>
  <div class="item"><div class="date">OCT . 25 , 12</div><h3 class="pub-title">Participative Geography, Information Science, and Politics</h3><p class="pub-text">Our WardMaker software, a tool that allows people to easily participate in creating election districts, has gotten some additional attention recently. We recently received an Outstanding Software Development Award ......</p></div>
  <p class="more">more publications...</p>
</section>

<aside>
  <div class="abs chirp"></div>
  <div class="abs chirp-head">Chirper ▾</div>
  <div class="abs chirp-tab-pop">Popular</div>
  <div class="abs chirp-tab-latest">Latest</div>
  <div class="abs scroll"></div>
  <div class="abs tweets">
    <div class="tweet"><div class="ago"><b>14</b> HOURS AGO</div><p class="t">Library Of the Assembly Completes Chirper Archive Through 2010</p></div>
    <div class="tweet"><div class="ago"><b>2</b> DAYS AGO</div><p class="t">Library Of the Assembly Completes Chirper Archive Through 2010</p></div>
    <div class="tweet"><div class="ago"><b>3</b> DAYS AGO</div><p class="t">Japan and Korea Lead New Year Mentions on Chirper</p></div>
    <div class="tweet"><div class="ago"><b>5</b> DAYS AGO</div><p class="t">Searchly Blocks ChirpPic, Lumen Denies Access to Chirper Pages</p></div>
    <div class="tweet"><div class="ago"><b>2</b> WEEKS AGO</div><p class="t">Postlyn Finally Lets Users Export Data, Will it Now Close?</p></div>
    <div class="tweet"><div class="ago"><b>2</b> WEEKS AGO</div><p class="t">Veracell: Marketing Firm Leaked Customer Data</p></div>
    <div class="tweet"><div class="ago"><b>3</b> WEEKS AGO</div><p class="t">Chirper Login Flaw Caused Passwords To Send In Plain Text</p></div>
    <div class="tweet"><div class="ago"><b>3</b> WEEKS AGO</div><p class="t">Dayloop Now Lets You Import All of Your Old Chirps</p></div>
  </div>
  <div class="abs tweet-to">Chirp to<small>@ Program for Knowledge Systems</small></div>
</aside>

<footer>
  <div class="abs footer-bar"></div>
  <div class="abs foot-brand" style="left:224px;top:1114px;font-size:18px">Varnell</div>
  <div class="abs foot-brand" style="left:290px;top:1123px;font-size:13px">Varnell Libraries</div>
  <div class="abs foot-link" style="left:402px">CONTACT US</div>
  <div class="abs foot-link" style="left:493px">FEEDBACK</div>
  <span class="abs foot-icon" style="left:565px" aria-label="Chirper"></span>
  <span class="abs foot-icon" style="left:585px" aria-label="Facepage"></span>
  <span class="abs foot-icon" style="left:606px" aria-label="News feed"></span>
</footer>
</body>
</html>
```